Austrian company needs an advertising banner / fence design

title
Construction fence banner

description
The company Trofal GmbH is a company which specializes in scaffolding & amp; Specializes in rental.
We are looking for a banner design for the labeling of a construction fence.
The idea from our side:
To place a caricature (employee) on a scaffold at the bottom left and right of the banner. These Trofal employees hang up an advertising banner together with the company data.

Company data: Trofal GmbH
Scaffolding & amp; rental
www.trofal.at
0664 -58 29 384

Information regarding logo:
Color red: RAL 3020 Pantone 485 C
Font: Trajan Pro

```html
<!DOCTYPE html>
<html lang="en">
<head>
<meta charset="utf-8">
<title>Trofal GmbH – Construction Fence Banner</title>
<link rel="stylesheet" href="https://fonts.googleapis.com/css2?family=Cinzel:wght@500;700&display=swap">
<style>
  :root {
    --stage: #b3b3b3;
    --scaffold-light: #dedede;
    --scaffold-dark: #8a8a8a;
    --panel: #ffffff;
    --ink: #1d1d1d;
    --band-dark: #222222;
    --signal-red: #e11d1a;
    --on-red: #ffffff;
  }
  * { margin: 0; padding: 0; box-sizing: border-box; }
  html, body {
    width: 901px;
    height: 1200px;
    overflow: hidden;
    background: var(--stage);
    font-family: "Cinzel", "Times New Roman", serif;
  }
  .banner {
    position: absolute;
    left: 20px;
    top: 296px;
    width: 860px;
    height: 608px;
    background: var(--scaffold-light);
    overflow: hidden;
  }
  .scaffold-art {
    position: absolute;
    inset: 0;
    background: linear-gradient(90deg, var(--scaffold-dark) 0%, var(--scaffold-light) 14%, var(--scaffold-light) 86%, var(--scaffold-dark) 100%);
  }
  .info-panel {
    position: absolute;
    left: 120px;
    top: 35px;
    width: 673px;
    height: 526px;
    background: var(--panel);
    border: 1px solid var(--ink);
  }
  .company-name {
    position: absolute;
    left: 0;
    right: 0;
    top: 62px;
    text-align: center;
    color: var(--ink);
    font-weight: 500;
    font-size: 74px;
    letter-spacing: 0.16em;
    line-height: 1;
  }
  .company-name .legal-form {
    font-size: 28px;
    letter-spacing: 0.04em;
  }
  .services {
    position: absolute;
    left: 0;
    right: 0;
    top: 225px;
    text-align: center;
    color: var(--ink);
    font-weight: 700;
    font-size: 50px;
    line-height: 68px;
  }
  .web-band {
    position: absolute;
    left: 120px;
    top: 408px;
    width: 673px;
    height: 53px;
    background: var(--band-dark);
    display: flex;
    align-items: center;
    justify-content: center;
    gap: 18px;
  }
  .web-band .rule {
    width: 110px;
    height: 2px;
    background: var(--signal-red);
  }
  .web-band .web-address {
    color: var(--on-red);
    font-weight: 500;
    font-size: 27px;
    letter-spacing: 0.18em;
  }
  .phone-band {
    position: absolute;
    left: 56px;
    top: 461px;
    width: 737px;
    height: 95px;
    background: var(--signal-red);
    display: flex;
    align-items: center;
    justify-content: center;
    padding-left: 64px;
  }
  .phone-band .phone-number {
    color: var(--on-red);
    font-weight: 700;
    font-size: 62px;
    letter-spacing: 0.02em;
  }
</style>
</head>
<body>
  <main class="banner">
    <div class="scaffold-art" role="img" aria-label="Scaffolding frame with worker silhouettes climbing and hanging the banner on the left and right"></div>

    <section class="info-panel">
      <h1 class="company-name">TROFAL <span class="legal-form">GmbH</span></h1>
      <p class="services">SCAFFOLDING<br>AND RENTAL</p>
    </section>

    <div class="web-band">
      <span class="rule"></span>
      <span class="web-address">WWW.TROFAL.AT</span>
      <span class="rule"></span>
    </div>

    <div class="phone-band">
      <span class="phone-number">0664 -58 29 384</span>
    </div>
  </main>
</body>
</html>
```